Website Design Needed for Fundmeadow-style Site

I need a design for a new website that is similar in concept in some ways to fundmeadow.example, but with a completely different market.

On one side, the site allows people to post projects for people to help fund, but where fundmeadow.example is focused on "creative" projects, this new site is focused on more serious "business-like" projects.

On the other side, the site allows visitors to help fund projects by pledging money in return for various rewards. In the attached image, ProjectDetailsConcept.png, the sidebar currently does not show the rewards mocked up, but there would need to be rewards listed there similar to what is shown here: http://www.fundmeadow.example/projects/torvel/paper-loop?ref=spotlight

The Project Details page will contain all the details for a given project. Note that some details are on different tabs on this page. Also note that the project description could be VERY long in some cases.

IMPORTANT: Although I have attached some concept images, please keep in mind that these are very rough and are mainly to illustrate what sort of content needs to be on the pages. None of the content on these mockup pages is final content.

Feel free to experiment with different layouts and concepts if you think they present the information better.

Pages Needed
1. Front Page - Shows main feature area, sub feature area, main menu, other links, search field and footer

2. Search/Browse Page - Lets users refine a search by clicking category names, locations, sort order, etc. Search results are listed below with next/prev controls and page number controls to navigate the results.

3. Project Details Page - Presents details of a given project. The specific details of the page content are not especially important. It is important that the Project Details Page allows multiple sections or tabs to be displayed though. The content in the sidebar of ProjectDetailsConcept.png is fairly representative of what might go there, especially in the top section of the sidebar. The top section should standout from the bottom section of the sidebar.

Keywords to try to relate in the site design: reliable, progressive, innovative, trustworthy, successful

Note that I do not yet have a logo for this site, but assume it is roughly the size and shape of the placeholder in the attached mockups.
Updates

I did some looking around at existing templates.

There are layout and color schemes in all of these that I like:

http://cms.layoutbarn.example/wordpress_41736/ (I quite like this one & it has dynamic)
http://38215.layouts.pagenook.example/
http://osc3.layoutbarn.example/stretched_27591/ (green with orange/yellow is nice)
http://images.osc3.layoutbarn.example/wt_35238/index.html

Also, please give consideration to the font choice for the site.  If necessary I can use cufon, Sifr or @fontface.

NOTE: I added another file called GreenHeaderMockup.png that is based on one of the website links in my previous update.

I like the body, but not the following aspects:

1. The header area needs some rework.  Maybe just a texture.

2. The project info for the featured project looks out of place.  Not sure where a better place would be, but see what comes to mind for you.

3. The project cards at the bottom are some variations...not sure which one I like the most.  Alternatives?

Feel free to ask questions.

Thanks.

Industry/Entity Type

Business

Requirements
Must have
• There must be a dynamic "Featured Projects" area near the top of the home page. This is similar in concept to the featured apps shown in the top of the Quillo Tool Bazaar. The set of available projects should somehow rotate or transition to focus on one project at a time while still leaving the others visible, but smaller. See the attached FrontPageConcept1.png image for a rough idea. Of course you are not responsible for coding the dynamic behavior, but you need to prepare the required graphical components to support any dynamic behavior you design.

The Search/Browse page must show a collection of "project cards", each of which contains some basic information about the project and an image. I have attached a file that shows some possible layouts for project cards.

See the attached SearchConcept1.png image for a concept that places all the search controls along the top, and the search results below. The concept shows two wide rows of project cards, but it would also be acceptable to show 4 rows of taller cards as in SearchConcept2.png

See the attached SearchConcept2.png image for a concept that places all the search controls in a sidebar, and the search results next to the sidebar. With this orientation, I think 3 tall project cards per row are all that can fit.

Should not have
• Must not use Flash or any other browser plugin.

```html
<!DOCTYPE html>
<html lang="en">
<head>
<meta charset="utf-8">
<title>Graphic Design – Browse Projects</title>
<link rel="stylesheet" href="https://fonts.googleapis.com/css2?family=Open+Sans:wght@400;600&family=Tinos:wght@400;700&family=Arimo:wght@400;700&display=swap">
<style>
:root{
  --green-dark:#1f5a06;
  --green:#3f8f0c;
  --green-bright:#7cc11d;
  --green-lime:#8fd42a;
  --green-text:#5aa514;
  --ink:#2a2a2a;
  --ink-soft:#555;
  --ink-muted:#777;
  --panel:#f1f1f1;
  --panel-line:#d9d9d9;
  --card:#f3f3f3;
  --white:#fff;
  --bar-dark:#2b2b2b;
}
*{box-sizing:border-box;margin:0;padding:0}
html,body{width:783px;height:1200px;overflow:hidden}
body{position:relative;background:var(--white);font-family:"Arimo",Arial,sans-serif;color:var(--ink)}
a{color:inherit;text-decoration:none}
ul{list-style:none}
h1,h2,h3,h4{font-weight:400}

/* header */
.site-header{position:absolute;left:0;top:0;width:783px;height:83px;
  background:
   repeating-linear-gradient(160deg,rgba(255,255,255,.06) 0 3px,transparent 3px 11px),
   radial-gradient(ellipse at 55% 10%,#6fbf1c 0%,#2f7d08 45%,#174c03 100%)}
.logo{position:absolute;left:30px;top:29px;font-family:"Tinos",serif;font-weight:700;font-size:26px;color:var(--white);letter-spacing:.3px}
.account-links{position:absolute;right:30px;top:21px;font-size:10px;color:#d9ef9a}
.account-links span{margin:0 8px;color:#a6d460}
.top-links{position:absolute;left:505px;top:49px;display:flex;gap:22px;font-family:"Tinos",serif;font-size:13px;color:var(--white)}
.social-top{position:absolute;left:690px;top:47px;display:flex;gap:20px}
.social-top i{width:19px;height:19px;background:#8dbf3a;border-radius:3px;opacity:.8}

/* nav */
.main-nav{position:absolute;left:0;top:83px;width:783px;height:37px;
  background:linear-gradient(#98dc36,#5eaa10 60%,#4c9608);border-bottom:1px solid #3d7c06}
.main-nav ul{display:flex;height:100%}
.main-nav li{font-family:"Tinos",serif;font-size:13.5px;color:var(--white);line-height:37px;padding:0 20px}
.main-nav li:first-child{margin-left:26px;background:var(--green-dark);padding:0 20px}
.main-nav li:nth-child(2){margin-left:6px}
.search{position:absolute;left:551px;top:5px;width:199px;height:26px;background:#f3f3f3;border:1px solid #bbb;border-radius:2px;font-size:10px;color:#666;line-height:24px;padding-left:8px}
.search svg{position:absolute;right:6px;top:4px}

/* filters */
.filters{position:absolute;left:0;top:133px;width:783px;height:151px;background:var(--panel);border-top:1px solid var(--panel-line);border-bottom:1px solid var(--panel-line)}
.filter-group{position:absolute;top:12px}
.filter-group h3{font-family:"Open Sans",sans-serif;font-weight:400;font-size:14.5px;color:var(--ink);padding-bottom:3px;border-bottom:1px solid #d0d0d0;margin-bottom:6px}
.filter-cols{display:flex}
.filter-group ul{font-size:10.5px;color:var(--ink-soft);line-height:15.4px;white-space:nowrap}
.g-cat{left:30px;width:209px}.g-cat ul{width:108px}
.g-feat{left:268px;width:110px}
.g-loc{left:401px;width:220px}.g-loc ul{width:108px}
.g-sort{left:646px;width:108px}

/* content */
.page-title{position:absolute;left:30px;top:303px;font-family:"Open Sans",sans-serif;font-size:18px;color:var(--ink)}
.page-title em{font-style:normal;color:var(--green-text)}
.section-title{position:absolute;left:50px;width:700px;display:flex;align-items:center;gap:8px;font-family:"Open Sans",sans-serif;font-size:13.5px;color:#444;letter-spacing:.3px}
.section-title::after{content:"";flex:1;border-top:1px dotted #b5b5b5}

.card{position:absolute;width:327px;height:247px;background:var(--card);border:1px solid #ddd;border-radius:4px;box-shadow:0 6px 8px -4px rgba(0,0,0,.25)}
.ribbon{position:absolute;left:80px;top:-5px;width:172px;height:29px;border-radius:2px;
  background:linear-gradient(#9ee23a,#5aaa10);box-shadow:0 2px 3px rgba(0,0,0,.3);
  font-family:"Open Sans",sans-serif;font-size:12.5px;color:var(--white);text-align:center;line-height:29px;letter-spacing:.4px}
.share{position:absolute;left:260px;top:8px;display:flex;gap:5px}
.share i{width:12px;height:12px;border-radius:2px}
.share i:nth-child(1){background:#333}.share i:nth-child(2){background:#4fb2e0}.share i:nth-child(3){background:#3b5a98}
.card-photo{position:absolute;left:16px;top:46px;width:129px;height:113px;border:3px solid var(--white);box-shadow:0 1px 3px rgba(0,0,0,.35)}
.card-meta{position:absolute;left:16px;top:166px;font-size:10.5px;color:var(--ink);line-height:16px}
.card-meta .place{display:flex;align-items:center;gap:4px}
.progress{margin-top:4px;width:131px;height:13px;background:var(--bar-dark);border-radius:2px;overflow:hidden}
.progress b{display:block;width:65%;height:100%;background:linear-gradient(#a6e445,#5ea915);font-size:8.5px;font-weight:400;color:#222;line-height:13px;padding-left:8px}
.card-title{position:absolute;left:162px;top:42px;font-family:"Open Sans",sans-serif;font-size:15px;color:var(--ink)}
.card-text{position:absolute;left:162px;top:67px;width:152px;font-size:9.3px;line-height:12px;color:var(--ink-muted);text-align:justify}
.see-more{position:absolute;display:flex;align-items:center;gap:6px;font-size:10.5px;color:var(--green-text)}

/* footer */
.footer{position:absolute;left:30px;top:1035px;width:720px;height:110px;border-top:1px dotted #bbb}
.footer h4{font-family:"Open Sans",sans-serif;font-size:13px;color:var(--ink);margin-bottom:9px}
.footer ul{font-size:10.5px;color:var(--ink-muted);line-height:15px}
.f-links{position:absolute;left:0;top:12px}
.f-cats{position:absolute;left:168px;top:12px}
.f-cats .filter-cols ul{width:108px}
.f-news{position:absolute;left:523px;top:12px;width:197px}
.f-news p{font-size:10px;color:var(--ink-muted)}
.email{margin-top:8px;width:175px;height:24px;background:#d4d4d4;border:1px solid #bbb;font-size:10px;color:#666;line-height:22px;padding-left:12px}
.subscribe{margin:10px 0 0 61px;width:64px;height:23px;border:1px solid #aaa;border-radius:3px;background:linear-gradient(#fff,#ddd);font-size:9.5px;text-align:center;line-height:21px;color:#333}

.bottom-bar{position:absolute;left:0;top:1157px;width:783px;height:43px;background:linear-gradient(#f6f6f6,#e6e6e6);border-top:1px solid #ddd}
.legal{position:absolute;left:30px;top:15px;display:flex;gap:14px;font-size:9px;color:var(--ink-muted);font-style:italic}
.legal span:first-child{color:#444}
.social-bottom{position:absolute;left:575px;top:9px;display:flex;gap:14px}
.social-bottom i{width:24px;height:24px;border-radius:3px}
</style>
</head>
<body>

<header class="site-header">
  <div class="logo">LOGO GOES HERE</div>
  <div class="account-links">Register<span>|</span>Login</div>
  <nav class="top-links"><a>Blog</a><a>FAQ</a><a>Company</a></nav>
  <div class="social-top"><i></i><i></i></div>
</header>

<nav class="main-nav">
  <ul><li>Features</li><li>Browse</li><li>My Account</li><li>Portfolio</li></ul>
  <div class="search">Search
    <svg width="16" height="16" viewBox="0 0 16 16"><circle cx="6.5" cy="6.5" r="4.5" fill="none" stroke="#333" stroke-width="1.8"/><line x1="10" y1="10" x2="14.5" y2="14.5" stroke="#333" stroke-width="2.4" stroke-linecap="round"/></svg>
  </div>
</nav>

<section class="filters">
  <div class="filter-group g-cat"><h3>Categories</h3>
    <div class="filter-cols">
      <ul><li>Category 1 name</li><li>Category 2 name</li><li>Category 3 name</li><li>Category 4 name</li><li>Category 7 name</li><li>Category 8 name</li></ul>
      <ul><li>Category 5 name</li><li>Category 6 name</li><li>Category 9 name</li><li>Category 10 name</li><li>Category 11 name</li><li>Category 12 name</li></ul>
    </div></div>
  <div class="filter-group g-feat"><h3>Featured</h3>
    <ul><li>Recommended</li><li>Popular</li><li>Recently Launched</li><li>Ending Soon</li><li>Small Projects</li><li>Most Funded</li></ul></div>
  <div class="filter-group g-loc"><h3>Locations</h3>
    <div class="filter-cols">
      <ul><li>New York</li><li>Los Angeles</li><li>Brooklyn</li><li>Chicago</li><li>San Francisco</li><li>Portland</li></ul>
      <ul><li>Seattle</li><li>Austin</li><li>New York</li><li>Boston</li><li>San Francisco</li><li>Chicago</li></ul>
    </div></div>
  <div class="filter-group g-sort"><h3>Sort By</h3>
    <ul><li>Recommended</li><li>Popular</li><li>Recently Launched</li><li>Ending Soon</li><li>Small Projects</li><li>Most Funded</li></ul></div>
</section>

<h1 class="page-title"><em>Design</em> / Graphic Design</h1>

<h2 class="section-title" style="top:336px">Popular This Week</h2>

<article class="card" style="left:40px;top:373px">
  <div class="ribbon">New &amp; Noteworthy</div>
  <div class="share"><i></i><i></i><i></i></div>
  <div class="card-photo" role="img" aria-label="Project photo: rider on a two-wheeled personal vehicle" style="background:linear-gradient(160deg,#8a8f96,#3c3e42 60%,#6d7075)"></div>
  <h3 class="card-title">Project Title Here</h3>
  <p class="card-text">Lorem ipsum dolor sit amet, consectetur adipisicing elit, sed do eiusmod tempor incididunt ut labore et dolore magna aliqua. Ut enim ad minim veniam, quis nostrud exercitation ullamco laboris nisi ut aliquip ex ea commodo consequat. Duis aute irure dolor in reprehenderit in voluptate velit esse cillum dolore eu fugiat nulla pariatur. Excepteur sint occaecat cupidatat non proident, sunt in culpa qui officia deserunt mollit anim id est</p>
  <div class="card-meta">
    <div class="place"><svg width="8" height="11" viewBox="0 0 8 11"><path d="M4 0a4 4 0 0 0-4 4c0 3 4 7 4 7s4-4 4-7a4 4 0 0 0-4-4z" fill="#222"/><circle cx="4" cy="4" r="1.5" fill="#f3f3f3"/></svg>Vancouver, B.C, Canada</div>
    <div>8 days left</div><div>Funded $65,000 of $100,000</div>
    <div class="progress"><b>65%</b></div>
  </div>
</article>

<article class="card" style="left:415px;top:373px">
  <div class="ribbon">Popular</div>
  <div class="share"><i></i><i></i><i></i></div>
  <div class="card-photo" role="img" aria-label="Project artwork: cartoon jungle scene for a sticker app" style="background:linear-gradient(160deg,#b7de4a,#3f9a1e 60%,#2c7012)"></div>
  <h3 class="card-title">Project Title Here</h3>
  <p class="card-text">Lorem ipsum dolor sit amet, consectetur adipisicing elit, sed do eiusmod tempor incididunt ut labore et dolore magna aliqua. Ut enim ad minim veniam, quis nostrud exercitation ullamco laboris nisi ut aliquip ex ea commodo consequat. Duis aute irure dolor in reprehenderit in voluptate velit esse cillum dolore eu fugiat nulla pariatur. Excepteur sint occaecat cupidatat non proident, sunt in culpa qui officia deserunt mollit anim id est</p>
  <div class="card-meta">
    <div class="place"><svg width="8" height="11" viewBox="0 0 8 11"><path d="M4 0a4 4 0 0 0-4 4c0 3 4 7 4 7s4-4 4-7a4 4 0 0 0-4-4z" fill="#222"/><circle cx="4" cy="4" r="1.5" fill="#f3f3f3"/></svg>Vancouver, B.C, Canada</div>
    <div>8 days left</div><div>Funded $65,000 of $100,000</div>
    <div class="progress"><b>65%</b></div>
  </div>
</article>

<a class="see-more" style="left:575px;top:650px"><svg width="14" height="6" viewBox="0 0 14 6"><path d="M0 3h12M9 0l3 3-3 3" fill="none" stroke="#5aa514" stroke-width="1.2"/></svg>See more popular projects</a>

<h2 class="section-title" style="top:672px">Recently Successful</h2>

<article class="card" style="left:40px;top:711px">
  <div class="ribbon">Closing Soon</div>
  <div class="share"><i></i><i></i><i></i></div>
  <div class="card-photo" role="img" aria-label="Project photo: costumed statue in an exhibition hall" style="background:linear-gradient(160deg,#c8ccc8,#5b6a5c 55%,#2e3430)"></div>
  <h3 class="card-title">Project Title Here</h3>
  <p class="card-text">Lorem ipsum dolor sit amet, consectetur adipisicing elit, sed do eiusmod tempor incididunt ut labore et dolore magna aliqua. Ut enim ad minim veniam, quis nostrud exercitation ullamco laboris nisi ut aliquip ex ea commodo consequat. Duis aute irure dolor in reprehenderit in voluptate velit esse cillum dolore eu fugiat nulla pariatur. Excepteur sint occaecat cupidatat non proident, sunt in culpa qui officia deserunt mollit anim id est</p>
  <div class="card-meta">
    <div class="place"><svg width="8" height="11" viewBox="0 0 8 11"><path d="M4 0a4 4 0 0 0-4 4c0 3 4 7 4 7s4-4 4-7a4 4 0 0 0-4-4z" fill="#222"/><circle cx="4" cy="4" r="1.5" fill="#f3f3f3"/></svg>Vancouver, B.C, Canada</div>
    <div>8 days left</div><div>Funded $65,000 of $100,000</div>
    <div class="progress"><b>65%</b></div>
  </div>
</article>

<article class="card" style="left:415px;top:711px">
  <div class="ribbon">Nearly Funded</div>
  <div class="share"><i></i><i></i><i></i></div>
  <div class="card-photo" role="img" aria-label="Project photo: hand sketching a flowchart on glass" style="background:linear-gradient(160deg,#f4f4f2,#d8d4cf 60%,#b49a86)"></div>
  <h3 class="card-title">Project Title Here</h3>
  <p class="card-text">Lorem ipsum dolor sit amet, consectetur adipisicing elit, sed do eiusmod tempor incididunt ut labore et dolore magna aliqua. Ut enim ad minim veniam, quis nostrud exercitation ullamco laboris nisi ut aliquip ex ea commodo consequat. Duis aute irure dolor in reprehenderit in voluptate velit esse cillum dolore eu fugiat nulla pariatur. Excepteur sint occaecat cupidatat non proident, sunt in culpa qui officia deserunt mollit anim id est</p>
  <div class="card-meta">
    <div class="place"><svg width="8" height="11" viewBox="0 0 8 11"><path d="M4 0a4 4 0 0 0-4 4c0 3 4 7 4 7s4-4 4-7a4 4 0 0 0-4-4z" fill="#222"/><circle cx="4" cy="4" r="1.5" fill="#f3f3f3"/></svg>Vancouver, B.C, Canada</div>
    <div>8 days left</div><div>Funded $65,000 of $100,000</div>
    <div class="progress"><b>65%</b></div>
  </div>
</article>

<a class="see-more" style="left:565px;top:985px"><svg width="14" height="6" viewBox="0 0 14 6"><path d="M0 3h12M9 0l3 3-3 3" fill="none" stroke="#5aa514" stroke-width="1.2"/></svg>See more successful projects</a>

<footer class="footer">
  <div class="f-links"><h4>Common Links</h4>
    <ul><li>My Account</li><li>Blog</li><li>Company</li><li>FAQ</li></ul></div>
  <div class="f-cats"><h4>Categories</h4>
    <div class="filter-cols">
      <ul><li>Category 1 name</li><li>Category 2 name</li><li>Category 3 name</li><li>Category 4 name</li></ul>
      <ul><li>Category 5 name</li><li>Category 6 name</li><li>Category 7 name</li><li>Category 8 name</li></ul>
      <ul><li>Category 9 name</li><li>Category 10 name</li><li>Category 11 name</li><li>Category 12 name</li></ul>
    </div></div>
  <div class="f-news"><h4>Newsletter</h4>
    <p>Subscribe to our newsletter for updates</p>
    <div class="email">Your email</div>
    <div class="subscribe">Subscribe</div></div>
</footer>

<div class="bottom-bar">
  <div class="legal"><span>Copyright 2011 Company INC.</span><span>Terms of Use</span><span>Privacy Policy</span><span>Contact Us</span></div>
  <div class="social-bottom">
    <i style="background:#c8201b"></i><i style="background:#38a9d9"></i><i style="background:#3b5a98"></i><i style="background:#f08a24"></i><i style="background:#5cc3e8"></i>
  </div>
</div>

</body>
</html>
```